Cyber Security Company Services Graphic

We need a 3D graphic of our services that resembles a great graphic that is used by another company. The image will be used on web sites, in presentations, and collateral. We will need to modify the text at some point as we change the name of the services. The attached file has the content that needs to be in our graphic (rough layout) and the example of a great graphic that we are using as the baseline for our image.

```html
<!DOCTYPE html>
<html lang="en">
<head>
<meta charset="utf-8">
<title>Managed Security Services Stack</title>
<link href="https://fonts.googleapis.com/css2?family=Nunito+Sans:wght@400;600&display=swap" rel="stylesheet">
<style>
  :root {
    --bg: #ffffff;
    --cloud: #e4e5e7;
    --cloud-deep: #d3d5d8;
    --orange: #f4462c;
    --orange-light: #ff7418;
    --orange-mid: #ee4a1a;
    --orange-dark: #c8330f;
    --icon-bg: #e8401c;
    --slate: #38444f;
    --deck: #585b5c;
    --deck-line: #6b6e6f;
    --label: #ea4a1c;
    --white: #ffffff;
  }
  html, body {
    margin: 0;
    padding: 0;
    width: 1200px;
    height: 640px;
    overflow: hidden;
    background: var(--bg);
  }
  .stack-graphic {
    display: block;
    width: 1200px;
    height: 640px;
    font-family: "Nunito Sans", sans-serif;
  }
  .callout-label {
    fill: var(--label);
    font-size: 10.5px;
    font-weight: 600;
    text-anchor: middle;
  }
  .callout-label.compact { font-size: 9.6px; }
  .leader {
    stroke: var(--slate);
    stroke-width: 1;
    stroke-dasharray: 1.5 2;
  }
  .tile { fill: var(--icon-bg); }
  .glyph {
    fill: none;
    stroke: var(--white);
    stroke-width: 1.3;
    stroke-linecap: round;
    stroke-linejoin: round;
  }
  .glyph-text {
    fill: var(--white);
    font-size: 9px;
    font-weight: 600;
    text-anchor: middle;
  }
  .block-front { fill: var(--orange); }
  .block-side { fill: var(--orange-dark); }
  .block-label {
    fill: var(--white);
    font-size: 12.5px;
    font-weight: 400;
    text-anchor: middle;
    letter-spacing: 0.2px;
  }
  .deck-top { fill: var(--deck); }
  .deck-line { stroke: var(--deck-line); stroke-width: 1.2; }
  .deck-front { fill: var(--slate); }
  .deck-label {
    fill: var(--white);
    font-size: 15.5px;
    font-weight: 400;
    text-anchor: middle;
    letter-spacing: 0.3px;
  }
  .platform-label {
    fill: var(--white);
    font-size: 19px;
    font-weight: 400;
    text-anchor: middle;
  }
</style>
</head>
<body>
<svg class="stack-graphic" viewBox="0 0 1200 640" xmlns="http://www.w3.org/2000/svg">
  <defs>
    <radialGradient id="cloudGlow" cx="50%" cy="55%" r="55%">
      <stop offset="0%" stop-color="var(--cloud-deep)"/>
      <stop offset="70%" stop-color="var(--cloud)"/>
      <stop offset="100%" stop-color="var(--cloud)" stop-opacity="0"/>
    </radialGradient>
    <linearGradient id="blockTop" x1="0" y1="0" x2="0" y2="1">
      <stop offset="0%" stop-color="var(--orange-light)"/>
      <stop offset="100%" stop-color="var(--orange-mid)"/>
    </linearGradient>
  </defs>

  <g class="cloud-backdrop" role="img" aria-label="Soft grey cloud bank behind the service stack">
    <ellipse cx="600" cy="360" rx="560" ry="290" fill="url(#cloudGlow)"/>
  </g>

  <g class="base-platform">
    <polygon class="deck-top" points="112,538 1144,538 1060,440 200,440"/>
    <g class="deck-grid">
      <line class="deck-line" x1="200" y1="538" x2="260" y2="440"/>
      <line class="deck-line" x1="330" y1="538" x2="370" y2="440"/>
      <line class="deck-line" x1="460" y1="538" x2="480" y2="440"/>
      <line class="deck-line" x1="590" y1="538" x2="595" y2="440"/>
      <line class="deck-line" x1="720" y1="538" x2="710" y2="440"/>
      <line class="deck-line" x1="850" y1="538" x2="825" y2="440"/>
      <line class="deck-line" x1="980" y1="538" x2="940" y2="440"/>
      <line class="deck-line" x1="1080" y1="538" x2="1020" y2="440"/>
    </g>
    <rect class="deck-front" x="112" y="538" width="1032" height="38"/>
    <text class="platform-label" x="628" y="564">NORTHWATCH PORTAL &amp; OPERATING SYSTEM</text>
  </g>

  <g class="enablement-row">
    <polygon fill="url(#blockTop)" points="212,474 422,474 444,450 264,450"/>
    <polygon fill="url(#blockTop)" points="432,474 692,474 688,450 444,450"/>
    <polygon fill="url(#blockTop)" points="701,474 897,474 876,450 692,450"/>
    <polygon fill="url(#blockTop)" points="906,474 1046,474 1000,450 880,450"/>
    <rect class="block-front" x="212" y="474" width="210" height="32"/>
    <rect class="block-front" x="432" y="474" width="260" height="32"/>
    <rect class="block-front" x="701" y="474" width="196" height="32"/>
    <rect class="block-front" x="906" y="474" width="140" height="32"/>
    <text class="block-label" x="317" y="494">CONSULTING &amp; ADVISORY</text>
    <text class="block-label" x="562" y="494">MARKETING &amp; SALES</text>
    <text class="block-label" x="799" y="494">REPORTS &amp; COMPLIANCE</text>
    <text class="block-label" x="976" y="494">TRAINING</text>
  </g>

  <g class="services-deck">
    <polygon class="deck-top" points="168,411 1098,411 1010,328 250,328"/>
    <g class="deck-grid">
      <line class="deck-line" x1="260" y1="411" x2="320" y2="366"/>
      <line class="deck-line" x1="380" y1="411" x2="410" y2="366"/>
      <line class="deck-line" x1="500" y1="411" x2="510" y2="366"/>
      <line class="deck-line" x1="620" y1="411" x2="620" y2="366"/>
      <line class="deck-line" x1="740" y1="411" x2="730" y2="366"/>
      <line class="deck-line" x1="860" y1="411" x2="830" y2="366"/>
      <line class="deck-line" x1="980" y1="411" x2="930" y2="366"/>
    </g>
    <rect class="deck-front" x="168" y="411" width="930" height="38"/>
    <text class="deck-label" x="616" y="436">MANAGED SECURITY SERVICES</text>
  </g>

  <g class="service-pillars">
    <polygon fill="url(#blockTop)" points="253,334 472,334 516,280 332,280"/>
    <polygon class="block-side" points="472,334 482,334 522,284 516,280"/>
    <polygon fill="url(#blockTop)" points="482,334 770,334 760,280 522,280"/>
    <polygon class="block-side" points="770,334 776,334 764,282 760,280"/>
    <polygon fill="url(#blockTop)" points="776,334 1005,334 944,280 766,280"/>
    <rect class="block-front" x="253" y="334" width="219" height="33"/>
    <rect class="block-front" x="482" y="334" width="288" height="33"/>
    <rect class="block-front" x="776" y="334" width="229" height="33"/>
    <text class="block-label" x="362" y="355">VULNERABILITY MANAGEMENT</text>
    <text class="block-label" x="626" y="355">24X7 CONTINUOUS DETECTION &amp; RESPONSE</text>
    <text class="block-label" x="890" y="355">GOVERNANCE, RISK &amp; COMPLIANCE</text>
  </g>

  <g class="capability-callouts">
    <line class="leader" x1="353" y1="184" x2="353" y2="254"/>
    <line class="leader" x1="395" y1="223" x2="395" y2="254"/>
    <line class="leader" x1="436" y1="184" x2="436" y2="254"/>
    <line class="leader" x1="479" y1="223" x2="479" y2="254"/>
    <line class="leader" x1="576" y1="184" x2="576" y2="254"/>
    <line class="leader" x1="618" y1="224" x2="618" y2="254"/>
    <line class="leader" x1="660" y1="180" x2="660" y2="254"/>
    <line class="leader" x1="702" y1="221" x2="702" y2="254"/>
    <line class="leader" x1="797" y1="186" x2="797" y2="254"/>
    <line class="leader" x1="839" y1="227" x2="839" y2="254"/>
    <line class="leader" x1="881" y1="186" x2="881" y2="254"/>
    <line class="leader" x1="923" y1="223" x2="923" y2="254"/>

    <text class="callout-label" x="353" y="164">HUMAN</text>
    <text class="callout-label" x="353" y="178">BEHAVIOR</text>
    <text class="callout-label" x="395" y="205">THREAT</text>
    <text class="callout-label" x="395" y="218">HUNTING</text>
    <text class="callout-label" x="436" y="164">VULNERABILITY</text>
    <text class="callout-label" x="436" y="178">ASSESSMENT</text>
    <text class="callout-label compact" x="481" y="205">VULNERABILITY</text>
    <text class="callout-label compact" x="481" y="218">MANAGEMENT</text>
    <text class="callout-label" x="576" y="164">ENDPOINT</text>
    <text class="callout-label" x="576" y="178">PROTECTION</text>
    <text class="callout-label" x="618" y="206">NETWORKS</text>
    <text class="callout-label" x="618" y="219">&amp; SERVERS</text>
    <text class="callout-label" x="660" y="175">CLOUD</text>
    <text class="callout-label" x="702" y="216">24X7 SOC</text>
    <text class="callout-label" x="797" y="181">TECHNOLOGY</text>
    <text class="callout-label" x="839" y="222">PEOPLE</text>
    <text class="callout-label" x="881" y="181">PROCESS</text>
    <text class="callout-label" x="923" y="205">CYBER</text>
    <text class="callout-label" x="923" y="218">INSURANCE</text>
  </g>

  <g class="capability-icons">
    <rect class="tile" x="333" y="254" width="39" height="39"/>
    <path class="glyph" d="M343,285 v-6 a10,10 0 1 1 16,-8 l3,5 h-3 v5 h-5 v4"/>
    <path class="glyph" d="M351,273 v-6 m-3,3 l3,-3 l3,3"/>

    <rect class="tile" x="375" y="254" width="39" height="39"/>
    <circle class="glyph" cx="394.5" cy="273.5" r="12"/>
    <ellipse class="glyph" cx="394.5" cy="275" rx="4.5" ry="6"/>
    <path class="glyph" d="M390,272 h-4 m13,0 h4 m-13,5 h-4 m13,0 h4"/>

    <rect class="tile" x="417" y="254" width="39" height="39"/>
    <circle class="glyph" cx="434" cy="271" r="9"/>
    <path class="glyph" d="M441,278 l7,7"/>
    <rect class="glyph" x="430.5" y="270" width="7" height="5"/>
    <path class="glyph" d="M432,270 v-2 a2,2 0 0 1 4,0 v2"/>

    <rect class="tile" x="459" y="254" width="39" height="39"/>
    <circle class="glyph" cx="478.5" cy="273.5" r="9"/>
    <path class="glyph" d="M478.5,261 v3 m0,19 v3 m-12.5,-12.5 h3 m19,0 h3 m-21,-9 l2,2 m13,13 l2,2 m0,-17 l-2,2 m-13,13 l-2,2"/>
    <rect class="glyph" x="475" y="273" width="7" height="5"/>

    <rect class="tile" x="557" y="254" width="39" height="39"/>
    <path class="glyph" d="M576.5,262 l10,4 v7 c0,7 -5,11 -10,13 c-5,-2 -10,-6 -10,-13 v-7 z"/>
    <path class="glyph" d="M572,274 h8 m-3,-3 l3,3 l-3,3"/>

    <rect class="tile" x="598" y="254" width="39" height="39"/>
    <rect class="glyph" x="606" y="263" width="23" height="6"/>
    <rect class="glyph" x="606" y="271" width="23" height="6"/>
    <rect class="glyph" x="606" y="279" width="23" height="6"/>

    <rect class="tile" x="641" y="254" width="39" height="39"/>
    <path class="glyph" d="M653,281 h15 a5,5 0 0 0 0,-10 a7,7 0 0 0 -13,-1 a5.5,5.5 0 0 0 -2,11 z"/>

    <rect class="tile" x="682" y="254" width="39" height="39"/>
    <path class="glyph" d="M713,270 a12,12 0 1 1 -3,-6 m0,-4 v4 h-4"/>
    <text class="glyph-text" x="701.5" y="277">24/7</text>

    <rect class="tile" x="777" y="254" width="39" height="39"/>
    <circle class="glyph" cx="796.5" cy="275" r="5"/>
    <path class="glyph" d="M796.5,270 v-6 m-5,9 l-6,-4 m16,4 l6,-4 m-14,6 l-5,7 m11,-7 l5,7"/>
    <circle class="glyph" cx="796.5" cy="262" r="1.8"/>
    <circle class="glyph" cx="784" cy="268" r="1.8"/>
    <circle class="glyph" cx="809" cy="268" r="1.8"/>

    <rect class="tile" x="819" y="254" width="39" height="39"/>
    <circle class="glyph" cx="838.5" cy="266" r="3"/>
    <circle class="glyph" cx="830" cy="268" r="2.5"/>
    <circle class="glyph" cx="847" cy="268" r="2.5"/>
    <path class="glyph" d="M832,284 a6.5,6.5 0 0 1 13,0 m-20,-3 a5,5 0 0 1 7,-5 m13,0 a5,5 0 0 1 7,5"/>

    <rect class="tile" x="861" y="254" width="39" height="39"/>
    <rect class="glyph" x="876" y="262" width="9" height="7"/>
    <rect class="glyph" x="867" y="279" width="9" height="7"/>
    <rect class="glyph" x="885" y="279" width="9" height="7"/>
    <path class="glyph" d="M880.5,269 v5 m-9,5 v-5 h18 v5"/>

    <rect class="tile" x="903" y="254" width="39" height="39"/>
    <path class="glyph" d="M922.5,262 l10,4 v7 c0,7 -5,11 -10,13 c-5,-2 -10,-6 -10,-13 v-7 z"/>
    <path class="glyph" d="M918,274 l3,3 l6,-6"/>
  </g>
</svg>
</body>
</html>
```